Velmarone Website Redesign

We need a redesign of the company website.

We're a company, based in the UK, called Velmarone. We develop software for the Healthcare Industry, used by medical professionals throughout the UK on a daily basis.

We have a suite of tools that form the Velmarone Platform, and all are web-based.

We want to communicate that our software is not only innovative but is the best available, easy to use, and provides exceptional quality and RoI.

Additionally, we want our existing customers to be able to see what else we can offer them.

A site map is attached.
Updates

Hi Everyone,

As we approach the deadline for submissions, we’ve shortlisted threedesigns that we felt were the best of the submissions and have asked thedesigners to make some additional changes and produce some content pages so wecan see what’s beneath the Home page in the rest of the site.

Thank you all for your submissions – there was an awful lot ofdisagreement among everyone here over which designs we thought were best andsome of those that haven’t made it into the final three were very well liked.

Those in the final three have been messaged individually and have theirdesigns as the only non-eliminated ones showing. We would ask at this stagethat anyone not in the final three please do no further work or submitadditional designs as we are approaching the deadline and will not be able toprovide sufficient feedback to allow any changes in a short space of time.

Kind regards,
The Velmarone Team

Target Market(s)

Nurses and medical professionals in western-speaking countries, most notably in the UK.

Predominantly, we expect it will be senior medical staff that will be viewing (and using) our website - some will be existing customers and some will be new or potential customers.

Industry/Entity Type

Medical

Requirements
Must have
• Area to showcase and provide information about products.
• Company information - who we are and why you should choose us.
• News and events - blog, archive newsletters, publications, etc.
• Support section for existing customers - FAQ, Forum, Manuals.
• Contact page.
• We also feel that we'd like to have our telephone number and primary email address visible at all times, with an immediate ability for users to request a demonstration.
Nice to have
• A "My Velmarone" area would be nice at some point, though that's something for further down the line.

```html
<!DOCTYPE html>
<html lang="en">
<head>
<meta charset="utf-8">
<title>Velmarone – Clinical Systems</title>
<link href="https://fonts.googleapis.com/css2?family=Arimo:wght@400;700&display=swap" rel="stylesheet">
<style>
  :root {
    --brand-blue: #1e7fc1;
    --link-blue: #3f86c6;
    --nav-active: #3b79bb;
    --nav-border: #a9c6e2;
    --nav-muted: #b8c9da;
    --sub-active: #c9d6e8;
    --ink: #1a1a1a;
    --cell-bg: #eef2f8;
    --grid-line: rgba(200, 210, 222, 0.35);
    --white: #ffffff;
  }
  * { box-sizing: border-box; margin: 0; padding: 0; }
  html, body { width: 1200px; height: 857px; overflow: hidden; background: var(--white); }
  body { position: relative; font-family: "Arimo", Arial, sans-serif; color: var(--ink); }

  .page-grid {
    position: absolute; left: 103px; top: 146px; width: 985px; height: 660px;
    background-image:
      linear-gradient(var(--grid-line) 1px, transparent 1px),
      linear-gradient(90deg, var(--grid-line) 1px, transparent 1px);
    background-size: 10px 10px;
  }

  .brand { position: absolute; left: 103px; top: 78px; display: flex; align-items: center; gap: 10px; }
  .brand-mark { width: 22px; height: 22px; background: var(--brand-blue); }
  .brand-name { font-size: 31px; font-weight: 700; color: var(--brand-blue); line-height: 34px; }

  .quick-icons { position: absolute; left: 936px; top: 84px; display: flex; gap: 26px; }
  .quick-icons svg { width: 26px; height: 26px; }

  .main-nav, .sub-nav, .account-bar { position: absolute; display: flex; }
  .main-nav { left: 105px; top: 206px; height: 23px; }
  .main-nav a, .sub-nav a, .account-bar span {
    display: flex; align-items: center; justify-content: center;
    text-decoration: none; border: 1px solid var(--nav-border); margin-left: -1px; white-space: nowrap;
  }
  .main-nav a { font-size: 10.5px; color: var(--nav-muted); background: var(--white); }
  .main-nav a.is-active { background: var(--nav-active); color: var(--white); border-color: var(--nav-active); }

  .sub-nav { left: 105px; top: 231px; height: 22px; }
  .sub-nav-band { position: absolute; left: 105px; top: 231px; width: 982px; height: 22px; background: linear-gradient(90deg, #f1f5fa, #fbfcfe); }
  .sub-nav a { font-size: 10.5px; color: #2a6fb0; background: var(--white); }
  .sub-nav a.is-active { background: var(--sub-active); font-weight: 700; }

  .product-grid {
    position: absolute; left: 105px; top: 253px; width: 982px; height: 466px;
    display: grid; grid-template-columns: 280px 378px 320px; grid-template-rows: repeat(3, 154px);
    gap: 2px; background: var(--white);
  }
  .product { position: relative; background: var(--cell-bg); overflow: hidden; padding: 8px 6px 0 8px; }
  .product-title { position: relative; z-index: 1; font-size: 15.5px; font-weight: 400; line-height: 18px; white-space: nowrap; letter-spacing: -0.1px; }
  .product-title em { font-style: normal; color: var(--link-blue); }
  .product-desc { position: relative; z-index: 1; font-size: 10.4px; line-height: 14px; margin-top: 1px; letter-spacing: -0.1px; }
  .product-visual { position: absolute; left: 0; right: 0; bottom: 0; }

  .visual-portrait { top: 50px; background: linear-gradient(180deg, rgba(238,242,248,0) 0%, rgba(238,242,248,0) 12%, transparent 13%), linear-gradient(90deg, #d8dde2 0%, #c9b6a6 35%, #e8e4e1 70%, #f3f4f6 100%); -webkit-mask-image: linear-gradient(180deg, transparent 0, #000 14px); mask-image: linear-gradient(180deg, transparent 0, #000 14px); }
  .visual-chart { top: 48px; background: linear-gradient(180deg, rgba(238,242,248,0) 0%, #e2e6ec 40%, #cfd5de 100%); }
  .visual-waves { top: 40px; background: linear-gradient(180deg, rgba(238,242,248,0) 0%, #c8d2e4 45%, #7e90b5 100%); }
  .visual-bars { top: 64px; background: linear-gradient(160deg, rgba(238,242,248,0) 0%, #c7d3ea 50%, #8ea8d6 100%); }
  .visual-folders { top: 46px; background: linear-gradient(120deg, rgba(238,242,248,0) 0%, #d6dbe6 40%, #b9c3d6 100%); }
  .visual-scans { top: 64px; background: linear-gradient(180deg, rgba(238,242,248,0) 0%, #b7bec8 45%, #6f7884 100%); }
  .visual-magnifier { top: 36px; background: linear-gradient(180deg, rgba(238,242,248,0) 0%, #dcdcdc 50%, #c7c2bf 100%); }

  .account-bar { left: 105px; top: 720px; height: 21px; }
  .account-bar span { font-size: 10.5px; background: var(--white); color: #2a6fb0; }
  .account-bar .account-label { background: var(--sub-active); color: var(--white); border-color: var(--sub-active); }
  .account-bar .account-field { color: #c8d2de; font-style: italic; border-color: #e3e9f0; }

  .footer-brand { position: absolute; left: 978px; top: 758px; display: flex; align-items: center; gap: 5px; }
  .footer-brand-mark { width: 9px; height: 9px; background: var(--brand-blue); }
  .footer-brand-name { font-size: 13px; font-weight: 700; color: var(--brand-blue); }
</style>
</head>
<body>
  <div class="page-grid"></div>

  <header class="brand">
    <span class="brand-mark"></span>
    <span class="brand-name">Velmarone</span>
  </header>

  <div class="quick-icons">
    <svg viewBox="0 0 26 26" aria-label="Email"><path d="M2 6 L24 4 L24 20 L2 22 Z" fill="#2f8fd0"/><path d="M2 6 L13 14 L24 4" fill="none" stroke="#a9d4f1" stroke-width="1.5"/></svg>
    <svg viewBox="0 0 26 26" aria-label="Feed"><rect x="4" y="3" width="16" height="20" rx="3" fill="#2f8fd0"/><circle cx="9" cy="18" r="1.8" fill="#fff"/><path d="M8 13 a5 5 0 0 1 5 5 M8 8.5 a9.5 9.5 0 0 1 9.5 9.5" fill="none" stroke="#fff" stroke-width="1.6"/></svg>
    <svg viewBox="0 0 26 26" aria-label="Downloads"><path d="M3 10 L13 4 L23 10 L13 16 Z" fill="#2f8fd0"/><path d="M3 14 L13 20 L23 14" fill="none" stroke="#2f8fd0" stroke-width="2"/><path d="M9 9 L13 11.5 L17 9" fill="none" stroke="#fff" stroke-width="1.2"/></svg>
  </div>

  <nav class="main-nav">
    <a class="is-active" href="#" style="width:149px">PRODUCTS &amp; SEVICES</a>
    <a href="#" style="width:133px">REQUEST A DEMO</a>
    <a href="#" style="width:131px">ABOUT VELMARONE</a>
    <a href="#" style="width:134px">NEWS &amp; EVENTS</a>
    <a href="#" style="width:118px">SUPPORT</a>
  </nav>

  <div class="sub-nav-band"></div>
  <nav class="sub-nav">
    <a class="is-active" href="#" style="width:149px">Clinical Systems</a>
    <a href="#" style="width:133px">Clinical Audit Tools</a>
    <a href="#" style="width:133px">Technology Services</a>
  </nav>

  <main class="product-grid">
    <article class="product">
      <div class="product-visual visual-portrait" role="img" aria-label="Photo of a smiling elderly patient"></div>
      <h2 class="product-title"><em>Cleft</em> Patient Management</h2>
      <p class="product-desc">An end-to-end electronic patient records solution for Cleft departments.</p>
    </article>
    <article class="product">
      <div class="product-visual visual-chart" role="img" aria-label="Photo of a printed schedule chart with a pen"></div>
      <h2 class="product-title"><em>Tissue Viability</em> Management</h2>
      <p class="product-desc">An online tool enabling Tissue Viability Nurses manage their patient visit schedules and track their patients wound treatment.</p>
    </article>
    <article class="product">
      <div class="product-visual visual-waves" role="img" aria-label="Image of a blue data line graph"></div>
      <h2 class="product-title"><em>HALCYON</em> - Infection Control Management</h2>
      <p class="product-desc">Real-time tracking and management of hospital infections.</p>
    </article>

    <article class="product">
      <div class="product-visual visual-bars" role="img" aria-label="Photo of a blue bar chart with a pen"></div>
      <h2 class="product-title">Pressure <em>Ulcer</em> Management</h2>
      <p class="product-desc">Electronic Pressure Ulcer Record System that tracks and reports on patients Pressure Ulcers, grading, progress or degradation.</p>
    </article>
    <article class="product">
      <div class="product-visual visual-folders" role="img" aria-label="Photo of colour-tabbed patient record folders"></div>
      <h2 class="product-title">Electronic <em>Patient Record</em></h2>
      <p class="product-desc">An integrated view of the patient’s electronic records through an intuitive, easy to use, web based portal.</p>
    </article>
    <article class="product">
      <div class="product-visual visual-scans" role="img" aria-label="Photo of radiology scans on a lightbox wall"></div>
      <h2 class="product-title"><em>Radiology</em> Information</h2>
      <p class="product-desc">Radiology Information System with full support for internal/ external electronic referrals, Radiology Workflow and DICOM Modality Integration.</p>
    </article>

    <article class="product">
      <div class="product-visual visual-magnifier" role="img" aria-label="Photo of a magnifying glass over a colourful bar chart"></div>
      <h2 class="product-title"><em>Ward and Bed</em> Management</h2>
      <p class="product-desc">Electronic ward and bed state tracking.</p>
    </article>
    <article class="product">
      <h2 class="product-title"><em>Patient Summary</em> Views</h2>
      <p class="product-desc">A patient toolkit that enables hospitals to define and create custom patient data views from multiple source systems.</p>
    </article>
    <article class="product">
      <h2 class="product-title">Patient <em>Medication Tracker</em></h2>
      <p class="product-desc">An electronic tracking tool for monitoring patients current and past medications.</p>
    </article>
  </main>

  <div class="account-bar">
    <span class="account-label" style="width:132px">MY-VELMARONE</span>
    <span class="account-field" style="width:130px">username</span>
    <span class="account-field" style="width:117px">password</span>
    <span style="width:132px">ACCOUNT SETTINGS</span>
    <span style="width:131px">LICENSES</span>
    <span style="width:119px">DOWNLOADS</span>
  </div>

  <footer class="footer-brand">
    <span class="footer-brand-mark"></span>
    <span class="footer-brand-name">Velmarone</span>
  </footer>
</body>
</html>
```